REALTOR/REALESTATE INVESTOR CARD

I AM MY LOCAL CITIES FLIP THIS HOUSE KING...I CHANGE NEIGHBORHOODS ONE HOUSE AT A TIME. I BUY OLD HOUSES FOR CASH TOTALLY RENOVATE THEM TO LIKE NEW, THEN RE SELL THEM...
I HAVE BEEN USING PLATINUM & BURGANDY AS MY MAIN COLOR..
I WANT SOMETHING FUN AND MODERN TO APPEAL TO ALL BUYERS AND SELLERS. AND TO REFLECT I AM AT THE TOP OF MY GAME...A WOW...THIS IS A GREAT CARD.......WOW.......I AM A REALTOR....I FLIP HOUSES.....MAYBE SHOW AND OLD HOUSE AND THEN A SPARKLING NEW HOUSE..... MY COMPANY NAME IS HARBORLINE PROPERTY PARTNERS THE ADDRESS IS P.O.BOX 738 GOOSE CREEK, S.C. 29445

Target Market(s)

I SELL HOUSES THAT HAVE BEEN RENOVATED TO ALMOST BRAND NEW CONDITION.......I ALSO BUY HOUSES/MOBILES FOR ALL CASH FAST CLOSINGS..
I BUY GOOSE CREEK HOUSES ALL CASH FAST CLOSE.....I BUY MOBILE HOMES ANY CONDITION, ANY PRICE.....Buyers & sellers of houses.....

Industry/Entity Type

Investment

Font styles to use
Sans Serif

Requirements
Must have
• I BUY GOOSE CREEK HOUSES ALL CASH FAST CLOSINGS......
CHANGING GOOSE CREEK, ONE HOUSE AT A TIME...
RAY T. ELLWOOD CIAS
REALTOR/CERTIFIED INVESTOR AGENT
HARBORLINE PROPERTY PARTNERS,LLC.
P.O. BOX 738
GOOSE CREEK, S.C. 29445
843-555-0172
RAYELLWOODHOUSES@QUILLMAIL.EXAMPLE
Nice to have
• GOOSE CREEK'S RE-HAB KING....
A actual picture of MAYBE A HOME BEING RENOVATED
TO ONE LOOKING AWESOME.....artwork
Should not have
• a picture of and old ugly home the a sparkling brand new one that is what I di I renovate homes.......

```html
<!DOCTYPE html>
<html lang="en">
<head>
<meta charset="utf-8">
<title>Harborline Property Partners – Business Card</title>
<link href="https://fonts.googleapis.com/css2?family=Montserrat:wght@400;500;700&display=swap" rel="stylesheet">
<style>
  :root {
    --page-bg: #e6e4e1;
    --platinum-light: #f4f4f2;
    --platinum: #e3e4e6;
    --platinum-deep: #c9cbcf;
    --burgundy: #7a1f33;
    --burgundy-deep: #561222;
    --burgundy-light: #962c44;
    --ink-burgundy: #6e1a2d;
    --ink-grey: #4a4c52;
    --text-platinum: #eceef1;
    --text-platinum-muted: #d3d6db;
    --rule-platinum: rgba(236,238,241,0.6);
  }
  * { margin: 0; padding: 0; box-sizing: border-box; }
  html, body {
    width: 1200px;
    height: 1155px;
    overflow: hidden;
    background: var(--page-bg);
    font-family: "Montserrat", Arial, sans-serif;
  }
  .canvas {
    width: 1200px;
    height: 1155px;
    display: flex;
    flex-direction: column;
    align-items: center;
    justify-content: center;
    gap: 40px;
  }
  .card {
    width: 900px;
    height: 514px;
    position: relative;
    overflow: hidden;
    box-shadow: 0 6px 18px rgba(0,0,0,0.18);
  }

  /* Front: contact side */
  .card-front {
    background: linear-gradient(135deg, var(--platinum-light) 0%, var(--platinum) 60%, var(--platinum-deep) 100%);
    color: var(--ink-burgundy);
    padding: 62px 70px 0 90px;
  }
  .card-front .edge-band {
    position: absolute;
    left: 0;
    top: 0;
    bottom: 0;
    width: 18px;
    background: linear-gradient(180deg, var(--burgundy-light), var(--burgundy-deep));
  }
  .card-front .title,
  .card-front .company {
    font-weight: 700;
    font-size: 30px;
    line-height: 1.25;
  }
  .card-front .tagline {
    margin-top: 26px;
    padding-left: 22px;
    font-size: 18px;
    font-weight: 500;
    line-height: 1.45;
    color: var(--ink-grey);
  }
  .card-front .contact {
    position: absolute;
    left: 112px;
    bottom: 58px;
    font-size: 18px;
    font-weight: 500;
    line-height: 1.55;
    color: var(--ink-grey);
  }
  .card-front .contact .email { margin-bottom: 12px; color: var(--ink-burgundy); }

  /* Back: brand side */
  .card-back {
    background: radial-gradient(ellipse at 45% 35%, var(--burgundy-light) 0%, var(--burgundy) 45%, var(--burgundy-deep) 100%);
    color: var(--text-platinum);
    padding: 70px 0 0 170px;
  }
  .card-back .title,
  .card-back .company {
    font-weight: 700;
    font-size: 30px;
    line-height: 1.25;
  }
  .card-back .rule {
    width: 420px;
    height: 1px;
    background: var(--rule-platinum);
    margin: 16px 0 22px 10px;
  }
  .card-back .slogan {
    padding-left: 34px;
    font-size: 15px;
    font-weight: 500;
    line-height: 1.6;
    letter-spacing: 1px;
    text-transform: uppercase;
    color: var(--text-platinum-muted);
  }
</style>
</head>
<body>
<main class="canvas">
  <section class="card card-front" aria-label="Business card front">
    <div class="edge-band"></div>
    <p class="title">Realtor/Certified Investor Agent</p>
    <p class="company">Harborline Property Partners,Llc</p>
    <div class="tagline">
      <p>I buy goose creek house all cash fast closings......</p>
      <p>Changing goose creek, one house at a time...</p>
      <p>Ray t. ellwood cias</p>
    </div>
    <div class="contact">
      <p class="email">rayellwoodhouses@quillmail.example</p>
      <p class="address">P.O BOX 738, GOOSE CREEK, S.C. 29445, 843-555-0172</p>
    </div>
  </section>

  <section class="card card-back" aria-label="Business card back">
    <p class="title">Realtor/Certified Investor Agent</p>
    <p class="company">Harborline Property Partners,Llc</p>
    <div class="rule"></div>
    <div class="slogan">
      <p>Goose Creek's Re-Hab King....</p>
      <p>Maybe a home being renovated</p>
      <p>to one looking awesome.....</p>
    </div>
  </section>
</main>
</body>
</html>
```